Single-sided business card for restaurant bellwether with new logo made on this site

Business card options with new logo including restaurant name, address, phone number and website. This business card is single-sided only and will be presented at the hostess desk for clients to take. I would like to see options based on a cream card background, a white card background, a yellow card background and a burgundy colored background. It needs to be elegant and traditional.

Target Market(s)

local and international crowd

Industry/Entity Type

restaurant

Contact Information for Business Card

address, website and phone number

Font styles to use
Serif

Colors
EE7325
F08F49
F5BC92
FAE3D3
FDF4ED

Requirements
Must have
• new logo, address, phone number, website
Should not have
• more than three colors

```html
<!DOCTYPE html>
<html lang="en">
<head>
<meta charset="utf-8">
<title>Bellwether business cards</title>
<link rel="stylesheet" href="https://fonts.googleapis.com/css2?family=EB+Garamond:wght@400;700&display=swap">
<style>
  :root {
    --page: #d6d6d6;
    --card-white: #f4f4f2;
    --card-cream: #fdf4ed;
    --ink: #3d1d1f;
    --gold: #e8a935;
    --burgundy: #452a2c;
  }
  * { box-sizing: border-box; margin: 0; padding: 0; }
  html, body {
    width: 1156px;
    height: 1200px;
    overflow: hidden;
    background: var(--page);
    font-family: "EB Garamond", Georgia, serif;
  }
  .sheet {
    position: relative;
    width: 1156px;
    height: 1200px;
  }
  .card {
    position: absolute;
    left: 128px;
    width: 900px;
    height: 512px;
    border-radius: 30px;
    overflow: hidden;
    box-shadow: 0 6px 14px rgba(0, 0, 0, 0.28);
  }
  .card--white { top: 60px; background: var(--card-white); }
  .card--cream { top: 628px; background: var(--card-cream); }
  .contact {
    position: absolute;
    left: 65px;
    top: 84px;
    color: var(--ink);
  }
  .contact__name {
    font-size: 38px;
    font-weight: 700;
    line-height: 1;
  }
  .contact__role {
    margin-top: 10px;
    font-size: 27px;
    font-weight: 400;
    color: var(--gold);
    line-height: 1;
  }
  .contact__address {
    margin-top: 34px;
    font-size: 26px;
    line-height: 33px;
    font-style: normal;
  }
  .contact__lines {
    margin-top: 20px;
    font-size: 26px;
    line-height: 33px;
    list-style: none;
  }
  .contact__lines b { font-weight: 700; }
  .band {
    position: absolute;
    top: 0;
    left: 578px;
    width: 252px;
    height: 100%;
    display: flex;
    align-items: center;
    justify-content: center;
  }
  .card--white .band { background: var(--gold); }
  .card--cream .band { background: var(--burgundy); }
  .brand {
    font-size: 30px;
    font-weight: 700;
    letter-spacing: 3px;
    text-transform: uppercase;
  }
  .card--white .brand { color: var(--ink); }
  .card--cream .brand { color: var(--gold); }
</style>
</head>
<body>
<main class="sheet">
  <section class="card card--white">
    <div class="contact">
      <h1 class="contact__name">Mateo Lindqvist</h1>
      <p class="contact__role">General Manager</p>
      <address class="contact__address">Jacaranda 415<br>Bahía Serena<br>Costa Azul CP 48210</address>
      <ul class="contact__lines">
        <li><b>T.</b> 555-214-0387</li>
        <li><b>E.</b> mateo@bellwether.com.mx</li>
        <li>www.bellwether.com.mx</li>
      </ul>
    </div>
    <div class="band">
      <span class="brand">Bellwether</span>
    </div>
  </section>

  <section class="card card--cream">
    <div class="contact">
      <h2 class="contact__name">Mateo Lindqvist</h2>
      <p class="contact__role">General Manager</p>
      <address class="contact__address">Jacaranda 415<br>Bahía Serena<br>Costa Azul CP 48210</address>
      <ul class="contact__lines">
        <li><b>T.</b> 555-214-0387</li>
        <li><b>E.</b> mateo@bellwether.com.mx</li>
        <li>www.bellwether.com.mx</li>
      </ul>
    </div>
    <div class="band">
      <span class="brand">Bellwether</span>
    </div>
  </section>
</main>
</body>
</html>
```